Corvexa New Website

We are looking for a designer to provide html and css designs for a fiber to the home company. We are changing from our previous Talvorne Communications to Corvexa Communications, and will be using the attached logo now. Our current site can be seen at http://www.talvorne-example.com

Target Market(s)

Cable TV, Internet and Home Phone

Coding

Coded - Design and coding required

Number of Pages Required

1 page

```html
<!DOCTYPE html>
<html lang="en">
<head>
<meta charset="utf-8">
<title>Corvexa Communications</title>
<link rel="stylesheet" href="https://fonts.googleapis.com/css2?family=Lato:wght@400;700&family=Open+Sans:wght@400;600;700;800&display=swap">
<style>
:root{
  --blue:#12398a;
  --blue-deep:#0b2f78;
  --orange:#f4831f;
  --ink:#1c1c1c;
  --text:#555;
  --muted:#777;
  --light:#f1f1f1;
  --footer:#141414;
  --white:#fff;
}
*{box-sizing:border-box;margin:0;padding:0}
html,body{width:1200px;height:4235px;overflow:hidden}
body{position:relative;background:var(--white);font-family:"Open Sans",Arial,sans-serif;color:var(--ink)}
.abs{position:absolute}
h2.section-title{font-family:"Lato",Arial,sans-serif;font-weight:400;font-size:46px;color:var(--ink)}
.btn{position:absolute;display:flex;align-items:center;justify-content:center;border-radius:30px;font-weight:700;font-size:15px;color:var(--white)}
.btn-orange{background:var(--orange)}
.btn-blue{background:var(--blue)}

/* hero */
.hero{position:absolute;left:0;top:0;width:1200px;height:700px;background:linear-gradient(90deg,#f4f3f1 0%,#ecebe8 45%,#e6e2dc 100%)}
.hero-photo{position:absolute;left:470px;top:0;width:730px;height:640px;background:radial-gradient(ellipse at 60% 40%,#e9d9c9 0%,#e2d6ca 35%,#eeeae6 70%,rgba(238,234,230,0) 100%)}
.brand{position:absolute;left:113px;top:40px;display:flex;align-items:center;gap:12px;font-family:"Open Sans",sans-serif;font-weight:800;font-size:26px;color:var(--blue)}
.brand .dot{width:30px;height:30px;border-radius:50%;background:var(--orange)}
.contact-top{position:absolute;top:22px;display:flex;align-items:center;gap:12px;font-size:15px}
.contact-top .ico{width:44px;height:44px;border-radius:50%;border:2px solid var(--blue);display:flex;align-items:center;justify-content:center}
.contact-top small{display:block;color:var(--blue);font-size:13px}
.contact-top b{font-weight:600;color:var(--ink)}
.nav{position:absolute;top:84px;left:404px;display:flex;gap:38px;font-size:13px;font-weight:600;text-transform:uppercase;color:var(--ink)}
.hero-title{position:absolute;left:112px;top:196px;font-weight:800;font-size:58px;line-height:62px;color:var(--blue-deep)}
.hero-sub{position:absolute;left:113px;top:330px;font-size:24px;color:#333}
.dots{position:absolute;left:540px;top:550px;display:flex;gap:14px}
.dots i{width:18px;height:18px;border-radius:50%;border:2px solid var(--ink);background:var(--white)}
.dots i:first-child{background:var(--ink)}

/* services */
.card{position:absolute;top:805px;width:220px;height:305px;background:var(--white);box-shadow:0 2px 10px rgba(0,0,0,.18);text-align:center}
.card .circle{width:92px;height:92px;border-radius:50%;background:#f0f0f0;margin:40px auto 0;display:flex;align-items:center;justify-content:center}
.card h3{font-size:19px;font-weight:600;margin-top:28px}
.card p{font-size:14px;line-height:22px;color:var(--muted);padding:10px 22px 0}
.services-text{position:absolute;left:848px;top:870px;width:270px;font-size:15px;line-height:28px;color:var(--muted)}

/* register */
.register h2{position:absolute;width:1200px;text-align:center;top:1340px;font-family:"Lato",sans-serif;font-weight:400;font-size:34px;color:var(--white)}
.register p{position:absolute;width:1200px;text-align:center;top:1395px;font-size:15px;color:var(--white)}
.btn-outline{position:absolute;left:432px;top:1460px;width:336px;height:54px;border:2px solid var(--white);border-radius:30px;color:var(--white);font-weight:600;font-size:16px;display:flex;align-items:center;justify-content:center}

/* why */
.why-item{position:absolute;top:1826px;width:260px;text-align:center}
.why-item .ring{width:176px;height:176px;border-radius:50%;border:3px solid var(--blue);margin:0 auto;display:flex;align-items:center;justify-content:center}
.why-item p{margin-top:36px;font-size:21px;line-height:31px;font-weight:600;color:var(--ink)}

/* about */
.about{position:absolute;left:0;top:2250px;width:1200px;height:607px;background:var(--light)}
.about-photo{position:absolute;left:113px;top:2357px;width:415px;height:381px;background:linear-gradient(135deg,#d9d7d2 0%,#bfb6a8 50%,#8f8778 100%);box-shadow:0 2px 10px rgba(0,0,0,.2)}
.about-text{position:absolute;left:582px;top:2462px;width:520px;font-size:15px;line-height:31px;color:#444}

/* blog */
.post{position:absolute;top:3060px;width:297px;height:384px}
.post .thumb{height:190px}
.post .body{position:absolute;left:14px;top:172px;width:269px;height:212px;background:var(--white);box-shadow:0 2px 10px rgba(0,0,0,.15);text-align:center;padding:22px 16px 0}
.post h4{font-size:17px;font-weight:400;line-height:26px;color:#222}
.post .date{margin-top:12px;font-size:15px;color:var(--blue);display:flex;gap:8px;justify-content:center;align-items:center}
.post p{margin-top:14px;font-size:13px;line-height:21px;color:var(--muted)}

/* footer */
.footer-col h5{font-family:"Lato",sans-serif;font-weight:700;font-size:24px;color:var(--white)}
.footer-text{font-size:12px;line-height:20px;color:#ddd}
.quick a{display:block;color:#ddd;font-size:14px;line-height:28px;text-decoration:none}
.contact-row{position:absolute;left:900px;display:flex;gap:16px;font-size:14px;line-height:20px;color:#ddd}
.contact-row .sq{width:28px;height:28px;border-radius:4px;background:var(--orange);display:flex;align-items:center;justify-content:center;flex:none;margin-top:4px}
.newsletter-input{position:absolute;left:361px;top:3873px;width:291px;height:40px;border-radius:20px;background:var(--white);font-size:13px;color:#555;padding:11px 18px}
.social{position:absolute;top:4151px;display:flex;gap:6px;left:516px}
.social i{width:36px;height:36px;border-radius:50%;border:2px solid #ccc}
.copyright{position:absolute;top:4104px;width:1200px;text-align:center;font-size:12px;color:#ddd}
</style>
</head>
<body>

<section class="hero">
  <div class="hero-photo" role="img" aria-label="Smiling woman on a sofa using her smartphone"></div>
  <div class="brand"><span class="dot"></span>Corvexa</div>
  <div class="contact-top" style="left:612px">
    <span class="ico"><svg width="20" height="20" viewBox="0 0 24 24"><path d="M6.6 10.8a15 15 0 0 0 6.6 6.6l2.2-2.2a1 1 0 0 1 1-.25 11.4 11.4 0 0 0 3.6.57 1 1 0 0 1 1 1V20a1 1 0 0 1-1 1A17 17 0 0 1 3 4a1 1 0 0 1 1-1h3.5a1 1 0 0 1 1 1c0 1.25.2 2.45.57 3.6a1 1 0 0 1-.25 1z" fill="#12398a"/></svg></span>
    <div><small>Call Us :</small><b>1.800.555.0142</b></div>
  </div>
  <div class="contact-top" style="left:844px">
    <span class="ico"><svg width="20" height="20" viewBox="0 0 24 24"><rect x="3" y="5" width="18" height="14" rx="2" fill="#12398a"/><path d="M3 7l9 6 9-6" stroke="#fff" stroke-width="1.8" fill="none"/></svg></span>
    <div><small>Email :</small><b>hello@corvexa-example.com</b></div>
  </div>
  <nav class="nav"><span>Residential</span><span>Commercial</span><span>TV Listings ▾</span><span>FAQs</span><span>My Account</span><span>Contact Us</span></nav>
  <h1 class="hero-title">Corvexa<br>Communications</h1>
  <p class="hero-sub">Say Goodbye to slow internet with fiber</p>
  <a class="btn btn-orange" style="left:113px;top:418px;width:212px;height:52px">CONTACT US NOW</a>
  <div class="dots"><i></i><i></i><i></i><i></i></div>
</section>
<svg class="abs" style="left:0;top:540px" width="1200" height="170" viewBox="0 0 1200 170">
  <path d="M0 95 C260 160 560 155 820 90 C980 50 1100 20 1200 5 L1200 170 L0 170 Z" fill="#fff"/>
  <path d="M0 95 C260 160 560 155 820 90 C980 50 1100 20 1200 5" fill="none" stroke="#12398a" stroke-width="7"/>
</svg>

<section class="services">
  <div class="card" style="left:88px">
    <div class="circle"><svg width="46" height="46" viewBox="0 0 24 24" fill="none" stroke="#12398a" stroke-width="1.5"><circle cx="12" cy="12" r="9"/><ellipse cx="12" cy="12" rx="4" ry="9"/><path d="M3 12h18M5 7h14M5 17h14"/></svg></div>
    <h3>Internet</h3><p>Lorem ipsum dolor sit amet, consectetur ing elit, sed do eiusmod tempor</p>
  </div>
  <div class="card" style="left:338px">
    <div class="circle"><svg width="46" height="46" viewBox="0 0 24 24" fill="none" stroke="#12398a" stroke-width="1.6"><rect x="3" y="4" width="18" height="12" rx="1"/><path d="M9 20h6M12 16v4"/></svg></div>
    <h3>Television</h3><p>Lorem ipsum dolor sit amet, consectetur ing elit, sed do eiusmod tempor</p>
  </div>
  <div class="card" style="left:588px">
    <div class="circle"><svg width="44" height="44" viewBox="0 0 24 24"><path d="M6.6 10.8a15 15 0 0 0 6.6 6.6l2.2-2.2a1 1 0 0 1 1-.25 11.4 11.4 0 0 0 3.6.57 1 1 0 0 1 1 1V20a1 1 0 0 1-1 1A17 17 0 0 1 3 4a1 1 0 0 1 1-1h3.5a1 1 0 0 1 1 1c0 1.25.2 2.45.57 3.6a1 1 0 0 1-.25 1z" fill="#12398a"/><path d="M14 3a7 7 0 0 1 7 7M14 6a4 4 0 0 1 4 4" stroke="#12398a" stroke-width="1.6" fill="none"/></svg></div>
    <h3>Telephone</h3><p>Lorem ipsum dolor sit amet, consectetur ing elit, sed do eiusmod tempor</p>
  </div>
  <h2 class="section-title abs" style="left:844px;top:795px">Our Services</h2>
  <p class="services-text">Lorem ipsum dolor sit amet, consectetur adipiscing elit, sed do eiusmod tempor incididunt ut labore et dolore magna aliqua. Ut enim ad minim veniam,</p>
  <a class="btn btn-orange" style="left:850px;top:1053px;width:150px;height:47px">Learn More</a>
</section>

<section class="register">
  <svg class="abs" style="left:0;top:1200px" width="1200" height="460" viewBox="0 0 1200 460">
    <defs><linearGradient id="regGrad" x1="0" y1="0" x2="1" y2="0.3"><stop offset="0" stop-color="#0c3a8f"/><stop offset="0.42" stop-color="#1a4590"/><stop offset="0.7" stop-color="#d77a2e"/><stop offset="1" stop-color="#f4831f"/></linearGradient></defs>
    <path d="M0 5 L1200 32 L1200 35 L0 35 Z" fill="#f4831f"/>
    <rect x="0" y="32" width="1200" height="400" fill="url(#regGrad)"/>
    <path d="M0 430 L1200 430 L1200 457 Z" fill="#f4831f"/>
  </svg>
  <h2>Register for Fiber Internet</h2>
  <p>We're always looking new areas to expand, so add your name to our list!</p>
  <a class="btn-outline">Click Here For Registration</a>
</section>

<section class="why">
  <h2 class="section-title abs" style="width:1200px;text-align:center;top:1750px">Why Choose Us</h2>
  <div class="why-item" style="left:170px">
    <div class="ring"><svg width="96" height="96" viewBox="0 0 48 48" fill="none" stroke="#12398a" stroke-width="2.2" stroke-linecap="round"><circle cx="28" cy="27" r="13"/><path d="M28 27V19M28 27l5 4M25 10h6M28 10v4M39 15l2-2M4 22h9M2 28h10M6 34h9"/></svg></div>
    <p>Up to 15x Faster<br>Than DSL</p>
  </div>
  <div class="why-item" style="left:471px">
    <div class="ring"><svg width="90" height="90" viewBox="0 0 48 48" fill="none" stroke="#12398a" stroke-width="2.2" stroke-linejoin="round"><path d="M22 5 L37 11 V23 C37 33 30 40 22 43 C14 40 7 33 7 23 V11 Z"/><path d="M22 10 L32 14 V23 C32 30 28 35 22 38"/><circle cx="31" cy="32" r="8" fill="#fff"/><path d="M27 32l3 3 5-6"/></svg></div>
    <p>More Reliable Than<br>Cable &amp; DSL</p>
  </div>
  <div class="why-item" style="left:769px">
    <div class="ring"><svg width="90" height="90" viewBox="0 0 48 48" fill="none" stroke="#12398a" stroke-width="2.2" stroke-linecap="round"><path d="M38 20 A15 15 0 1 0 36 34"/><path d="M38 12v8h-8"/><text x="18" y="31" font-family="Open Sans,sans-serif" font-size="16" font-weight="700" fill="#12398a" stroke="none">$</text><path d="M33 38l4 3 5-4" /></svg></div>
    <p>Best Prices In Town.<br>Period</p>
  </div>
</section>

<svg class="abs" style="left:0;top:2212px" width="1200" height="40" viewBox="0 0 1200 40"><path d="M0 4 L1200 38 L0 38 Z" fill="#12398a"/></svg>
<section class="about"></section>
<div class="about-photo" role="img" aria-label="Person relaxing in a bright living room with a wall-mounted TV"></div>
<h2 class="section-title abs" style="left:579px;top:2370px">About Us</h2>
<p class="about-text">Lorem ipsum dolor sit amet, consectetur adipiscing elit, sed do eiusmod tempor incididunt ut labore et dolore magna aliqua. Ut enim ad minim veniam, quis nostrud exercitation ullamco laboris nisi ut aliquip ex ea commodo consequat. Duis aute irure dolor in reprehenderit in voluptate velit esse cillum dolore eu fugiat nulla pariatur.</p>
<a class="btn btn-blue" style="left:584px;top:2670px;width:150px;height:46px">READ MORE</a>
<svg class="abs" style="left:0;top:2855px" width="1200" height="30" viewBox="0 0 1200 30"><path d="M750 0 L1200 0 L1200 28 Z" fill="#12398a"/></svg>

<section class="blog">
  <h2 class="section-title abs" style="width:1200px;text-align:center;top:2968px">Latest Blog</h2>
  <article class="post" style="left:155px">
    <div class="thumb" role="img" aria-label="Glowing blue network cubes" style="background:linear-gradient(135deg,#0b3a4a,#1aa6b8 55%,#063040)"></div>
    <div class="body"><h4>Sed ut perspiciatis unde omnis iste natus</h4><div class="date"><svg width="14" height="14" viewBox="0 0 24 24"><rect x="3" y="5" width="18" height="16" rx="2" fill="#12398a"/><rect x="5" y="10" width="14" height="9" fill="#fff"/></svg>Oct 01, 2019</div><p>Sed ut perspiciatis unde omnis iste natus error sit voluptatem accusan tium doreque laudantium, totam</p></div>
  </article>
  <article class="post" style="left:494px">
    <div class="thumb" role="img" aria-label="Hand holding a bundle of fiber optic cables" style="background:linear-gradient(135deg,#e8e6e2,#c79a5c 55%,#d9d5cf)"></div>
    <div class="body"><h4>Sed ut perspiciatis unde omnis iste natus</h4><div class="date"><svg width="14" height="14" viewBox="0 0 24 24"><rect x="3" y="5" width="18" height="16" rx="2" fill="#12398a"/><rect x="5" y="10" width="14" height="9" fill="#fff"/></svg>Oct 01, 2019</div><p>Sed ut perspiciatis unde omnis iste natus error sit voluptatem accusan tium doreque laudantium, totam</p></div>
  </article>
  <article class="post" style="left:833px">
    <div class="thumb" role="img" aria-label="Remote control pointed at a television screen" style="background:linear-gradient(135deg,#2f5c9c,#c9d3e0 50%,#7a3a2a)"></div>
    <div class="body"><h4>Sed ut perspiciatis unde omnis iste natus</h4><div class="date"><svg width="14" height="14" viewBox="0 0 24 24"><rect x="3" y="5" width="18" height="16" rx="2" fill="#12398a"/><rect x="5" y="10" width="14" height="9" fill="#fff"/></svg>Oct 01, 2019</div><p>Sed ut perspiciatis unde omnis iste natus error sit voluptatem accusan tium doreque laudantium, totam</p></div>
  </article>
</section>

<footer>
  <svg class="abs" style="left:0;top:3500px" width="1200" height="735" viewBox="0 0 1200 735">
    <path d="M0 40 C250 110 600 180 850 110 C1000 70 1120 45 1200 35 L1200 735 L0 735 Z" fill="#f4831f"/>
    <path d="M0 70 C250 160 600 225 850 155 C1000 112 1120 95 1200 90 L1200 735 L0 735 Z" fill="#141414"/>
  </svg>
  <div class="abs" style="left:104px;top:3780px;display:flex;align-items:center;gap:10px;font-weight:800;font-size:24px;color:#fff"><span style="width:26px;height:26px;border-radius:50%;background:#fff"></span>Corvexa</div>
  <div class="footer-col abs" style="left:361px;top:3752px;width:300px">
    <h5>Sign up for newsletter</h5>
    <p class="footer-text" style="margin-top:18px">Excepteur sint occaecat cupidatat non proident, sunt in culpa qui officia deserunt</p>
  </div>
  <div class="newsletter-input">Enter email</div>
  <a class="btn btn-orange" style="left:361px;top:3930px;width:122px;height:36px;font-size:13px">SIGN UP</a>
  <div class="footer-col quick abs" style="left:709px;top:3752px">
    <h5>Quick Links</h5>
    <div style="margin-top:8px"><a>Residential</a><a>Commercial</a><a>TV Listings</a><a>Fiber</a><a>FAQs</a><a>My Account</a><a>Contact Us</a></div>
  </div>
  <div class="footer-col abs" style="left:900px;top:3752px"><h5>Contact Us</h5></div>
  <div class="contact-row" style="top:3820px"><span class="sq"><svg width="14" height="14" viewBox="0 0 24 24"><path d="M12 2a7 7 0 0 0-7 7c0 5 7 13 7 13s7-8 7-13a7 7 0 0 0-7-7zm0 9.5a2.5 2.5 0 1 1 0-5 2.5 2.5 0 0 1 0 5z" fill="#fff"/></svg></span><div>Corvexa<br>725 Harlow Avenue, 9th floor<br>Brookfield, NY 10452</div></div>
  <div class="contact-row" style="top:3888px"><span class="sq"><svg width="14" height="14" viewBox="0 0 24 24"><path d="M6.6 10.8a15 15 0 0 0 6.6 6.6l2.2-2.2a1 1 0 0 1 1-.25 11.4 11.4 0 0 0 3.6.57 1 1 0 0 1 1 1V20a1 1 0 0 1-1 1A17 17 0 0 1 3 4a1 1 0 0 1 1-1h3.5a1 1 0 0 1 1 1c0 1.25.2 2.45.57 3.6a1 1 0 0 1-.25 1z" fill="#fff"/></svg></span><div>Call us today:<br>1.800.555.0142</div></div>
  <div class="contact-row" style="top:3945px"><span class="sq"><svg width="14" height="14" viewBox="0 0 24 24"><rect x="3" y="5" width="18" height="14" rx="2" fill="#fff"/><path d="M3 7l9 6 9-6" stroke="#f4831f" stroke-width="1.8" fill="none"/></svg></span><div>Email :<br>hello@corvexa-example.com</div></div>
  <p class="copyright">© Copyright 2019 The Company Name. All Rights Reserved.</p>
  <div class="social"><i></i><i></i><i></i><i></i></div>
</footer>

</body>
</html>
```